Design WORDPRESS Website for E Commerce Business

We are needing a WORDPRESS website for an E Commerce Business that is supplying quailty kids / baby products.

Target Market(s)

Female / Working Mums / New Mums

Industry/Entity Type

Business

Number of Pages Required

1 page

Font styles to use
Sans Serif

Colors
33b8a4
f8fcfd
d3a5cc
f7f1f7
cbcbcb
9d9d9d

```html
<!DOCTYPE html>
<html lang="en">
<head>
<meta charset="utf-8">
<title>Cubby &amp; Co — Kids &amp; Baby Store</title>
<link rel="stylesheet" href="https://fonts.googleapis.com/css2?family=Roboto:wght@400;500;700&family=Courgette&family=Fredoka:wght@500&display=swap">
<style>
:root{
  --teal:#33b8a4;
  --pink:#f47ee3;
  --pink-btn:#c77fbd;
  --mint:#d5f4ec;
  --ink:#1a1a1a;
  --text:#444;
  --muted:#9d9d9d;
  --line:#cbcbcb;
  --card:#ebebeb;
  --white:#fff;
}
*{box-sizing:border-box;margin:0;padding:0}
html,body{width:1200px;height:3051px;overflow:hidden;background:#fff;font-family:'Roboto',Arial,sans-serif;color:var(--ink)}
.page{position:absolute;left:22px;top:0;width:1136px;height:3051px;background:#fff;box-shadow:0 0 14px rgba(0,0,0,.18)}
.abs{position:absolute}

/* top bar */
.topbar{left:0;top:0;width:1136px;height:50px;background:var(--teal);color:#fff;font-size:12px}
.topbar .phone{left:62px;top:17px;display:flex;align-items:center;gap:8px}
.topbar .social{display:flex;gap:10px;margin-left:12px}
.topbar .links{right:62px;top:17px;display:flex;gap:22px}
.scallop{left:0;top:44px;width:1136px;height:10px}

/* header */
.logo{display:flex;align-items:center;gap:10px;font-weight:700;color:var(--teal);font-size:34px;line-height:1;white-space:nowrap}
.logo .dot{width:40px;height:40px;border-radius:50%;background:#8a8a8a}
.site-logo{left:62px;top:84px}
.search{left:650px;top:70px;width:252px;height:36px;border:1px solid var(--line);border-radius:18px;overflow:hidden;display:flex}
.search span{flex:1;font-size:12px;color:var(--muted);padding:11px 16px}
.search b{width:36px;background:var(--pink-btn);display:flex;align-items:center;justify-content:center}
.cart{left:954px;top:78px;display:flex;align-items:center;gap:10px;font-size:13px;color:var(--text)}
.nav-item{top:132px;font-size:15px;color:var(--ink);transform:translateX(-50%);white-space:nowrap}
.nav-item.active{color:var(--pink)}

/* hero */
.hero{left:0;top:179px;width:1136px;height:543px;background:linear-gradient(180deg,#86d8f0 0%,#4cc0e8 40%,#33aedb 78%,#b8c2c5 90%,#a3aaac 100%)}
.hero-title{left:554px;top:150px;font-family:'Courgette',cursive;font-size:50px;color:#fff;white-space:nowrap}
.hero-btn{left:552px;top:240px;width:140px;height:40px;background:var(--pink);color:#fff;font-size:13px;display:flex;align-items:center;justify-content:center}
.hero-arrow{top:214px;width:40px;height:40px;border:2px solid rgba(255,255,255,.85);border-radius:50%}

/* features */
.feature{top:790px;width:320px;height:122px;border:1px solid var(--teal);display:flex}
.feature .icon{width:140px;height:120px;background:var(--teal);clip-path:polygon(0 0,78% 0,100% 50%,78% 100%,0 100%);display:flex;align-items:center;padding-left:24px}
.feature .copy{padding:36px 0 0 6px}
.feature h3{font-size:16px;font-weight:700;color:var(--ink)}
.feature p{font-size:14px;color:var(--pink);margin-top:6px}

/* section heads */
.sec-title{font-size:28px;font-weight:700;color:var(--ink);letter-spacing:.3px}
.sec-rule{height:2px;background:#e3e3e3}
.sec-accent{height:4px;width:42px;background:var(--pink)}
.round-arrow{width:30px;height:30px;border-radius:50%;border:2px solid #222;display:flex;align-items:center;justify-content:center}
.round-arrow.pink{border-color:var(--pink)}

/* product grid */
.product{width:320px;height:302px}
.product .shot{height:254px;background:var(--card);position:relative}
.product .art{position:absolute;left:70px;top:24px;width:180px;height:150px;border-radius:30px}
.product .name{position:absolute;left:0;right:0;top:198px;text-align:center;font-size:20px;color:#333}
.product .bar{height:48px;display:flex;font-size:16px}
.product .add{width:162px;background:var(--teal);color:#fff;display:flex;align-items:center;justify-content:center;gap:8px}
.product .price{flex:1;background:#0d0d0d;color:#fff;display:flex;align-items:center;justify-content:center;font-size:20px}

/* promo */
.promo{top:1735px;width:486px;height:225px;overflow:hidden;background:linear-gradient(120deg,#f4e6dc,#d9b79b 60%,#bfa08a)}
.promo .wedge{position:absolute;left:0;top:0;height:225px;width:230px;background:var(--pink);clip-path:polygon(0 0,70% 0,100% 50%,70% 100%,0 100%)}
.promo h4{position:absolute;left:20px;font-size:38px;font-weight:700;color:#fff;line-height:1.1}
.promo p{position:absolute;left:20px;font-size:34px;color:#fff}

/* offers */
.offer{top:2083px;width:234px;height:256px;border:1px solid var(--line);text-align:center}
.offer .art{width:130px;height:110px;margin:24px auto 0;border-radius:40% 50% 40% 50%;background:linear-gradient(135deg,#e2cdb6,#b8967a)}
.offer .title{font-size:15px;color:#333;margin-top:14px}
.offer .stars{margin-top:8px;display:flex;justify-content:center}
.offer .price{font-size:20px;font-weight:700;margin-top:6px}

/* brands */
.brand{top:2400px;width:194px;height:104px;border:1px solid var(--line);display:flex;align-items:center;justify-content:center;font-size:24px;font-weight:700;white-space:nowrap}

/* newsletter */
.dash{left:0;width:1136px;border-top:2px dashed var(--teal)}
.nl-title{left:194px;top:2586px;font-family:'Fredoka',sans-serif;font-weight:500;font-size:30px;color:var(--pink)}
.nl-form{left:382px;top:2585px;width:556px;height:44px;border:1px solid var(--pink);border-radius:22px;overflow:hidden;display:flex}
.nl-form span{flex:1;font-size:13px;color:var(--muted);padding:14px 24px}
.nl-form b{width:130px;background:var(--pink);color:#fff;font-weight:400;font-size:18px;display:flex;align-items:center;justify-content:center}

/* footer */
.footer{left:0;top:2707px;width:1136px;height:344px;background:var(--mint)}
.f-logo{left:62px;top:44px}
.f-about{left:62px;top:140px;width:480px;font-size:13px;line-height:24px;color:#444}
.f-social{left:62px;top:262px;display:flex;gap:18px;font-size:12px;color:#2b2b2b;font-weight:700}
.f-col h5{font-size:22px;font-weight:500;color:var(--teal)}
.f-col .rule{width:42px;height:3px;background:var(--pink);margin:10px 0 12px}
.f-col li{list-style:none;font-size:15px;color:#333;line-height:38px}
.f-contact li{list-style:none;font-size:15px;color:#333;line-height:26px;display:flex;gap:10px;margin-bottom:12px}
.f-pay{left:754px;top:290px;display:flex;gap:22px;font-size:15px;font-weight:700}
</style>
</head>
<body>
<div class="page">

  <div class="abs topbar">
    <div class="abs phone">
      <svg width="12" height="12" viewBox="0 0 24 24" fill="#fff"><path d="M6.6 10.8a15 15 0 0 0 6.6 6.6l2.2-2.2c.3-.3.7-.4 1-.2 1.1.4 2.3.6 3.6.6.6 0 1 .4 1 1V20c0 .6-.4 1-1 1A17 17 0 0 1 3 4c0-.6.4-1 1-1h3.5c.6 0 1 .4 1 1 0 1.3.2 2.5.6 3.6.1.3 0 .7-.2 1z"/></svg>
      555-014-2290
      <div class="social"><span>Circlo</span><span>Chirpr</span><span>Plusly</span><span>Snapgram</span></div>
    </div>
    <div class="abs links"><span>♥ Wish list</span><span>Create Account</span><span>Login</span></div>
  </div>
  <svg class="abs scallop" viewBox="0 0 1136 10" preserveAspectRatio="none">
    <defs><pattern id="sc" width="12" height="10" patternUnits="userSpaceOnUse"><circle cx="6" cy="0" r="6" fill="#33b8a4"/></pattern></defs>
    <rect width="1136" height="10" fill="url(#sc)"/>
  </svg>

  <div class="abs logo site-logo"><span class="dot"></span>Cubby &amp; Co</div>
  <div class="abs search"><span>Search for product</span><b><svg width="14" height="14" viewBox="0 0 24 24" fill="none" stroke="#fff" stroke-width="3"><circle cx="10" cy="10" r="6"/><path d="M15 15l5 5"/></svg></b></div>
  <div class="abs cart">
    <svg width="26" height="22" viewBox="0 0 26 22" fill="#33b8a4"><path d="M2 8h22l-3 12H5z"/><path d="M8 8l5-6 5 6" fill="none" stroke="#33b8a4" stroke-width="2"/></svg>
    0 item - $0.00
  </div>
  <nav>
    <span class="abs nav-item active" style="left:426px">Home</span>
    <span class="abs nav-item" style="left:518px">Boy ▾</span>
    <span class="abs nav-item" style="left:596px">Girl</span>
    <span class="abs nav-item" style="left:680px">Shoes</span>
    <span class="abs nav-item" style="left:778px">Brands</span>
    <span class="abs nav-item" style="left:868px">Sale</span>
    <span class="abs nav-item" style="left:948px">Blog</span>
    <span class="abs nav-item" style="left:1042px">Contact</span>
  </nav>

  <section class="abs hero" role="img" aria-label="Banner photo of two young children in colourful outfits standing by a blue sea railing">
    <div class="abs hero-arrow" style="left:14px"></div>
    <div class="abs hero-arrow" style="right:14px"></div>
    <div class="abs hero-title">Fashion for Childrens!</div>
    <div class="abs hero-btn">SHOP NOW</div>
  </section>

  <div class="abs feature" style="left:62px">
    <div class="icon"><svg width="62" height="44" viewBox="0 0 62 44" fill="#fff"><rect x="2" y="4" width="34" height="26" rx="2"/><path d="M38 12h12l8 10v8H38z"/><circle cx="14" cy="36" r="6"/><circle cx="48" cy="36" r="6"/></svg></div>
    <div class="copy"><h3>FREE SHIPPING</h3><p>24/7, including holiday</p></div>
  </div>
  <div class="abs feature" style="left:408px">
    <div class="icon"><svg width="58" height="54" viewBox="0 0 58 54" fill="none" stroke="#fff" stroke-width="4"><path d="M8 26l20-10 20 10v20L28 54 8 46z" fill="#fff"/><path d="M30 14A16 16 0 1 1 52 30"/><path d="M24 8l6 6-6 6"/></svg></div>
    <div class="copy"><h3>FREE RETURNS</h3><p>ipsum primis in faucib</p></div>
  </div>
  <div class="abs feature" style="left:754px">
    <div class="icon"><svg width="58" height="58" viewBox="0 0 58 58" fill="none" stroke="#fff" stroke-width="3"><rect x="12" y="22" width="36" height="32" stroke-dasharray="5 4"/><circle cx="10" cy="8" r="5"/><circle cx="22" cy="8" r="5"/><path d="M14 12l10 10M18 12L8 22"/><path d="M22 46l16-16"/><circle cx="24" cy="32" r="3"/><circle cx="36" cy="44" r="3"/></svg></div>
    <div class="copy"><h3>MEMBER DISCOUNT</h3><p>ipsum primis in faucib</p></div>
  </div>

  <h2 class="abs sec-title" style="left:62px;top:964px">NEW ARRIVALS</h2>
  <div class="abs sec-accent" style="left:62px;top:1004px"></div>
  <div class="abs round-arrow" style="left:1001px;top:972px"><svg width="10" height="12" viewBox="0 0 10 12"><path d="M7 1L2 6l5 5" fill="none" stroke="#222" stroke-width="2"/></svg></div>
  <div class="abs round-arrow pink" style="left:1043px;top:972px"><svg width="10" height="12" viewBox="0 0 10 12"><path d="M3 1l5 5-5 5" fill="none" stroke="#f47ee3" stroke-width="2"/></svg></div>

  <div class="abs product" style="left:62px;top:1040px"><div class="shot"><div class="art" role="img" aria-label="Photo of a turtle ride-on toy" style="background:linear-gradient(135deg,#6bbf3a,#f2d52a,#e24b2b)"></div><div class="name">Kids Toy</div></div><div class="bar"><div class="add"><svg width="18" height="16" viewBox="0 0 26 22" fill="#fff"><path d="M2 8h22l-3 12H5z"/></svg>Add to Cart</div><div class="price">$122.00</div></div></div>
  <div class="abs product" style="left:408px;top:1040px"><div class="shot"><div class="art" role="img" aria-label="Photo of a blue toy car" style="background:linear-gradient(135deg,#bfe3f7,#6fb4e6,#3c4c5c)"></div><div class="name">Kids Toy</div></div><div class="bar"><div class="add"><svg width="18" height="16" viewBox="0 0 26 22" fill="#fff"><path d="M2 8h22l-3 12H5z"/></svg>Add to Cart</div><div class="price">$122.00</div></div></div>
  <div class="abs product" style="left:754px;top:1040px"><div class="shot"><div class="art" role="img" aria-label="Photo of a push-along walker toy" style="background:linear-gradient(135deg,#f2a74a,#f5e04a,#e066c6)"></div><div class="name">Kids Toy</div></div><div class="bar"><div class="add"><svg width="18" height="16" viewBox="0 0 26 22" fill="#fff"><path d="M2 8h22l-3 12H5z"/></svg>Add to Cart</div><div class="price">$122.00</div></div></div>

  <div class="abs product" style="left:62px;top:1372px"><div class="shot"><div class="art" role="img" aria-label="Photo of a wooden baby walker" style="background:linear-gradient(135deg,#f0dcc0,#caa57e,#6e5a48)"></div><div class="name">Kids Toy</div></div><div class="bar"><div class="add"><svg width="18" height="16" viewBox="0 0 26 22" fill="#fff"><path d="M2 8h22l-3 12H5z"/></svg>Add to Cart</div><div class="price">$122.00</div></div></div>
  <div class="abs product" style="left:408px;top:1372px"><div class="shot"><div class="art" role="img" aria-label="Photo of pink children's sandals" style="background:linear-gradient(135deg,#fbd2e6,#f06aa8,#e9e9e9)"></div><div class="name">Kids Toy</div></div><div class="bar"><div class="add"><svg width="18" height="16" viewBox="0 0 26 22" fill="#fff"><path d="M2 8h22l-3 12H5z"/></svg>Add to Cart</div><div class="price">$122.00</div></div></div>
  <div class="abs product" style="left:754px;top:1372px"><div class="shot"><div class="art" role="img" aria-label="Photo of colourful baby rattles" style="background:linear-gradient(135deg,#f4e34a,#6cc44c,#e44a4a)"></div><div class="name">Kids Toy</div></div><div class="bar"><div class="add"><svg width="18" height="16" viewBox="0 0 26 22" fill="#fff"><path d="M2 8h22l-3 12H5z"/></svg>Add to Cart</div><div class="price">$122.00</div></div></div>

  <div class="abs promo" style="left:62px" role="img" aria-label="Photo of a baby in a hooded towel with a teething toy">
    <div class="wedge"></div>
    <h4 style="top:64px">Baby Store</h4>
    <p style="top:114px">50% Off</p>
  </div>
  <div class="abs promo" style="left:588px;background:linear-gradient(120deg,#f1e9e4,#d9c8c0 55%,#a89486)" role="img" aria-label="Photo of a baby in a knitted hat lying on a blanket">
    <div class="wedge"></div>
    <h4 style="top:38px">Exclusive<br>Offer</h4>
    <p style="top:132px">Soft Toys</p>
  </div>

  <h2 class="abs sec-title" style="left:62px;top:2014px">OUR OFFER</h2>
  <div class="abs sec-rule" style="left:62px;top:2052px;width:1012px"></div>
  <div class="abs sec-accent" style="left:62px;top:2052px"></div>
  <svg class="abs" style="left:1030px;top:2024px" width="44" height="16" viewBox="0 0 44 16" fill="none" stroke-width="2"><path d="M10 2L4 8l6 6" stroke="#222"/><path d="M34 2l6 6-6 6" stroke="#33b8a4"/></svg>

  <svg width="0" height="0" class="abs"><defs><path id="st" d="M7 0l2 5h5l-4 3 2 5-5-3-5 3 2-5-4-3h5z"/></defs></svg>
  <div class="abs offer" style="left:62px"><div class="art" role="img" aria-label="Photo of knitted baby booties"></div><div class="title">Maecenas imperdiet sagittis</div><div class="stars"><svg width="90" height="14" viewBox="0 0 90 14"><g fill="#33b8a4"><use href="#st"/><use href="#st" x="18"/><use href="#st" x="36"/></g><g fill="none" stroke="#33b8a4"><use href="#st" x="54"/><use href="#st" x="72"/></g></svg></div><div class="price">$122.00</div></div>
  <div class="abs offer" style="left:321px"><div class="art" role="img" aria-label="Photo of knitted baby booties"></div><div class="title">Maecenas imperdiet sagittis</div><div class="stars"><svg width="90" height="14" viewBox="0 0 90 14"><g fill="#33b8a4"><use href="#st"/><use href="#st" x="18"/><use href="#st" x="36"/></g><g fill="none" stroke="#33b8a4"><use href="#st" x="54"/><use href="#st" x="72"/></g></svg></div><div class="price">$122.00</div></div>
  <div class="abs offer" style="left:580px"><div class="art" role="img" aria-label="Photo of knitted baby booties"></div><div class="title">Maecenas imperdiet sagittis</div><div class="stars"><svg width="90" height="14" viewBox="0 0 90 14"><g fill="#33b8a4"><use href="#st"/><use href="#st" x="18"/><use href="#st" x="36"/></g><g fill="none" stroke="#33b8a4"><use href="#st" x="54"/><use href="#st" x="72"/></g></svg></div><div class="price">$122.00</div></div>
  <div class="abs offer" style="left:840px"><div class="art" role="img" aria-label="Photo of knitted baby booties"></div><div class="title">Maecenas imperdiet sagittis</div><div class="stars"><svg width="90" height="14" viewBox="0 0 90 14"><g fill="#33b8a4"><use href="#st"/><use href="#st" x="18"/><use href="#st" x="36"/></g><g fill="none" stroke="#33b8a4"><use href="#st" x="54"/><use href="#st" x="72"/></g></svg></div><div class="price">$122.00</div></div>

  <div class="abs brand" style="left:62px;color:#e8527a">TinyNest</div>
  <div class="abs brand" style="left:266px;color:#8cbf3a">Sprout Lane</div>
  <div class="abs brand" style="left:472px;color:#e28a1e">Bloomkin</div>
  <div class="abs brand" style="left:676px;color:#7a3f9a">Pipola</div>
  <div class="abs brand" style="left:880px;color:#e0457b">Waddle Wear</div>

  <div class="abs dash" style="top:2563px"></div>
  <div class="abs dash" style="top:2650px"></div>
  <div class="abs nl-title">NewsLetter</div>
  <div class="abs nl-form"><span>Your Email address</span><b>Subscribe</b></div>

  <footer class="abs footer">
    <div class="abs logo f-logo"><span class="dot" style="background:#2f8f80"></span>Cubby &amp; Co</div>
    <p class="abs f-about">Lorem Ipsum is simply dummy text of the printing and typesetting industry. Lorem Ipsum has been the industry's standard dummy text ever since the 1500s, when an unknown printer took a galley of type and scrambled it to make a type specimen book. It has survived not only five centuries</p>
    <div class="abs f-social"><span>Circlo</span><span>Chirpr</span><span>Plusly</span><span>Snapgram</span></div>

    <div class="abs f-col" style="left:622px;top:30px">
      <h5>Account</h5><div class="rule"></div>
      <ul><li>› Addresses</li><li>› Credit slips</li><li>› Orders</li><li>› Personal info</li></ul>
    </div>
    <div class="abs f-col f-contact" style="left:838px;top:30px;width:280px">
      <h5>Keep in touch</h5><div class="rule"></div>
      <ul>
        <li><svg width="12" height="12" viewBox="0 0 24 24" fill="#33b8a4" style="margin-top:7px;flex:none"><path d="M22 2L2 10l9 3 3 9z"/></svg><span>12 Orchard Row - Maple Court -<br>Riverton Lane - Riverton</span></li>
        <li><svg width="12" height="12" viewBox="0 0 24 24" fill="#33b8a4" style="margin-top:7px;flex:none"><path d="M22 2L2 10l9 3 3 9z"/></svg><span>555. 014. 2290 - 555. 014. 7731</span></li>
        <li><svg width="14" height="12" viewBox="0 0 24 20" fill="#33b8a4" style="margin-top:7px;flex:none"><path d="M2 2h20v16H2z"/><path d="M2 2l10 8 10-8" fill="none" stroke="#d5f4ec" stroke-width="2"/></svg><span>hello@cubbyco.example</span></li>
      </ul>
    </div>
    <div class="abs f-pay">
      <span style="color:#1d3b8f">Cardo</span>
      <span style="color:#d9452b">Plexa</span>
      <span style="color:#2f7fc1">Veltra</span>
      <span style="color:#1b4a8e">Quikpay</span>
      <span style="color:#c8102e">Shipro</span>
    </div>
  </footer>
</div>
</body>
</html>
```